Website Design : Design the digital space for the UK’s coolest offline movement – Pebblestone June

Think 1990s throwback meets modern minimalism—analogue culture brought into the now. The site should evoke a sense of a cool, fun rebellion. It should feel like an intentional lifestyle movement, not a corporate campaign.

Task Description:
We’re looking for a creative website designer to build a visually engaging, easy-to-navigate website for Pebblestone June CIC, a new UK-based social impact initiative encouraging individuals and families to reduce smartphone and social media use during April each year.
The site must be fully WIX-compatible, mobile-responsive, and built with accessibility, clarity, and inspiration in mind. The tone is bold but friendly—similar to Hatchwick UK—with clear calls to action, high readability, and a confident identity. It should feel like a positive challenge, not a guilt trip.

See Website Design Brief attached.
See Website Content (written content for the website) attached.
Draft logo included in attachments.
Updates

While 'Analogue' may invoke a sepia coloured world, we want this to website to be cool : vibrant, bold, energetic and expressive. Maybe even a little rebellious! It should be highly visual and communicate the energy and enthusiasm behind the 'analogue movement'! Possibly look at featuring a layered mix of saturated colours, playful typography, and a dynamic, urban edge.

Maybe look at using a vivid mix of neon tones contrasted with darker outlines and shadowing to make elements pop. Graffiti even? Graffiti wall textures, paint splatters, brick walls, and spray can motifs can be used subtly as background layers. Urban environments, street scenes, murals, community gatherings, and artistic expression.

We appreciate the target audience is rather wide, and understand its a big ask to appeal to such a wide group - Parents and Families (Ages 30–50), Professionals and Conscious Consumers (Ages 25–45), Teenagers and Young Adults (Ages 13–25), Schools and Educators, Mental Health Advocates, Researchers, and Funders.

Food for thought:
https://brevlink.example/d/qTzW8kP

Target Market(s)

Parents and Families (Aged 30–50), Professionals and Conscious Consumers (Aged 25–45), Teenagers & Young Adults (Aged 13–25), Schools & Educators, Funders, Supporters & Partners

Industry/Entity Type

Digital Wellbeing and Behavioural Health Campaigning, Public Mental Health and Lifestyle Awareness, Technology & Wellbeing Education (Nonprofit Sector)

Font styles to use
Other font styles liked:
• • Primary Font: Old-school typewriter-style serif font for headers (e.g. "Courier New", "American Typewriter", or retro fonts like "IBM Plex Mono") • Body Font: Clean, modern sans-serif (e.g. "Inter", "Lato", or "Raleway") for readability

```html
<!DOCTYPE html>
<html lang="en">
<head>
<meta charset="utf-8">
<title>Pebblestone June – Support Us</title>
<link rel="stylesheet" href="https://fonts.googleapis.com/css2?family=Courier+Prime:wght@400;700&family=Raleway:wght@400;500;600&display=swap">
<style>
:root{
  --green:#93b01f;
  --green-dark:#7f9a16;
  --sky:#8fb3c8;
  --sky-text:#9ab7cc;
  --cyan:#6fd3e0;
  --ink:#1e1e1e;
  --navy:#1f2b3d;
  --muted:#666;
  --panel:#f1f1f1;
  --white:#fff;
  --line:#e2e2e2;
}
*{box-sizing:border-box;margin:0;padding:0}
html,body{width:1200px;height:4175px;overflow:hidden}
body{font-family:"Raleway",sans-serif;color:var(--ink);background:var(--white);position:relative}
.abs{position:absolute}
.heading{font-family:"Courier Prime",monospace;font-weight:700;letter-spacing:1px}
.brand{font-family:"Courier Prime",monospace;font-size:16px;display:flex;align-items:center;gap:10px;color:var(--ink)}
.brand-square{width:26px;height:26px;border:2px solid var(--ink)}

/* header */
.site-header{top:0;left:0;width:1200px;height:109px;border-bottom:1px solid var(--line)}
.site-header .brand{left:144px;top:17px}
.auth{top:17px;display:flex;gap:10px;right:144px}
.auth a{display:block;height:35px;line-height:35px;padding:0 18px;color:#fff;font-size:13px;font-weight:600;text-decoration:none;text-transform:uppercase}
.auth .login{background:var(--sky)}
.auth .register{background:var(--green)}
.main-nav{left:144px;top:78px;width:912px;display:flex;justify-content:space-between;font-size:14px;font-weight:500}
.main-nav a{color:var(--ink);text-decoration:none;padding-bottom:8px}
.main-nav a.active{color:var(--green);border-bottom:2px solid var(--green)}

/* hero */
.hero{top:109px;left:0;width:1200px;height:561px;background:linear-gradient(90deg,#4c4b48 0%,#6e6d69 45%,#8a8a86 70%,#5a5f70 100%)}
.hero h1{position:absolute;left:144px;top:128px;font-size:54px;color:#fff;letter-spacing:3px}
.hero .lead{position:absolute;left:144px;top:206px;font-size:20px;color:var(--cyan)}
.hero p.copy{position:absolute;left:144px;top:248px;width:440px;font-size:17px;line-height:29px;color:#fff}
.btn-donate{position:absolute;left:144px;top:402px;width:159px;height:47px;background:var(--green);color:#fff;font-weight:700;font-size:15px;display:flex;align-items:center;justify-content:center;gap:8px;text-transform:uppercase}
.hero .arrows{position:absolute;left:562px;top:506px;display:flex;gap:28px}

/* raise funds */
.raise{top:670px;left:0;width:1200px;height:627px;background:linear-gradient(180deg,#fff,#f7f7f7)}
.section-title{font-size:34px;text-align:center}
.raise .section-title{position:absolute;top:62px;width:100%}
.raise .intro{position:absolute;left:150px;top:114px;width:900px;text-align:center;font-size:16px;line-height:29px;color:#333}
.raise .ideas{position:absolute;top:226px;width:100%;text-align:center;font-size:16px;font-weight:500;color:var(--navy);text-transform:uppercase}
.idea-card{position:absolute;background:#fff;box-shadow:0 3px 14px rgba(0,0,0,.09);display:flex;gap:18px;padding:24px 26px}
.idea-card svg{flex:none;margin-top:2px}
.idea-card h3{font-size:16px;font-weight:500;margin-bottom:12px}
.idea-card p{font-size:13px;line-height:23px;color:#555}

/* split panels */
.split{left:0;width:1200px}
.photo{position:absolute}
.panel-title{font-size:34px;position:absolute}
.panel-text{position:absolute;font-size:16px;line-height:29px;color:#333}
.label{position:absolute;font-size:15px;color:var(--sky-text);text-transform:uppercase}
.item{position:absolute}
.item h4{font-size:16px;font-weight:500;display:flex;align-items:center;gap:10px}
.item h4::before{content:"";width:10px;height:10px;background:var(--green)}
.item p{font-size:13px;line-height:23px;color:#555;margin-top:14px}

.donate{top:1297px;height:524px;background:var(--panel)}
.resources{top:1821px;height:538px;background:var(--panel)}
.resources .link{position:absolute;left:666px;top:456px;width:390px;font-size:13px;line-height:21px;color:var(--sky-text)}

/* events */
.events{top:2359px;height:576px;background:linear-gradient(135deg,#8db0c5,#9bbccf 60%,#89adc2)}
.events .section-title{position:absolute;top:60px;width:100%;color:#fff}
.events .intro{position:absolute;top:114px;width:100%;text-align:center;color:#fff;font-size:14px}
.events .upcoming{position:absolute;top:158px;width:100%;text-align:center;color:#fff;font-size:16px;font-weight:500;text-transform:uppercase}
.event-card{position:absolute;top:208px;height:287px}
.event-tag{position:absolute;background:#fff;text-align:center}
.slider-btn{position:absolute;top:342px;width:24px;height:24px;border:1.5px solid #fff;display:flex;align-items:center;justify-content:center}

/* where funds go */
.funds{top:2935px;height:612px;background:#fff}
.funds .title{position:absolute;left:144px;top:52px;font-size:34px}
.funds .sub{position:absolute;left:144px;top:114px;font-size:16px;font-weight:500;color:var(--navy);text-transform:uppercase}
.funds .nav{position:absolute;left:980px;top:58px;display:flex;gap:4px}
.charity{position:absolute;top:170px;width:291px}
.charity .thumb{height:208px}
.charity h4{font-size:16px;font-weight:500;margin-top:32px}
.charity p{font-size:13px;line-height:23px;color:#666;margin-top:14px}

/* strategic */
.strategic{top:3547px;height:475px;background:var(--green)}
.strategic .panel-title{left:144px;top:48px;color:#fff;line-height:48px}
.strategic .item h4{color:#fff}
.strategic .item h4::before{background:#fff}
.strategic .item p{color:#fff;margin-top:10px}

/* footer */
.site-footer{top:4022px;left:0;width:1200px;height:153px;background:#fff}
.site-footer .brand{position:absolute;left:144px;top:56px}
.contact{position:absolute;top:56px;display:flex;align-items:center;gap:10px;font-size:14px;color:#333}
.site-footer .rule{position:absolute;left:144px;top:104px;width:912px;border-top:1px dashed #bbb}
.site-footer .copy{position:absolute;left:150px;top:126px;font-size:13px;color:#555}
</style>
</head>
<body>

<header class="site-header abs">
  <div class="brand abs"><span class="brand-square"></span>Pebblestone June</div>
  <div class="auth abs">
    <a class="login" href="#">&#128274; Login</a>
    <a class="register" href="#">&#9998; Register</a>
  </div>
  <nav class="main-nav abs">
    <a class="active" href="#">SUPPORT US</a>
    <a href="#">ABOUT US</a>
    <a href="#">SMARTPHONE HEALTH</a>
    <a href="#">DIGITAL CHALLENGES</a>
    <a href="#">BLOG &amp; RESOURCES</a>
  </nav>
</header>

<section class="hero abs" role="img" aria-label="Photo of a smiling man in a white shirt wearing headphones and holding a cassette tape and a small camera, against a concrete wall">
  <h1 class="heading">SUPPORT US</h1>
  <div class="lead">Pebblestone June Is More Than Just A Digital Detox</div>
  <p class="copy">It's A Movement To Reclaim Our Time, Focus,&amp;Mental Well-being. Whether You're Going Full Analogue or Cheering From The Sidelines, There Are Plenty of Ways To Get Involved.</p>
  <a class="btn-donate">Donate
    <svg width="14" height="14" viewBox="0 0 14 14"><circle cx="7" cy="7" r="7" fill="#fff"/><path d="M5.5 4l3 3-3 3" stroke="#93b01f" stroke-width="2" fill="none"/></svg>
  </a>
  <div class="arrows">
    <svg width="22" height="24" viewBox="0 0 22 24"><path d="M20 2L2 12l18 10z" fill="none" stroke="#fff" stroke-width="1.6"/></svg>
    <svg width="22" height="24" viewBox="0 0 22 24"><path d="M2 2l18 10L2 22z" fill="#fff"/></svg>
  </div>
</section>

<section class="raise abs">
  <h2 class="section-title heading">Raise Funds</h2>
  <p class="intro">Turn Your Smartphone Sabbatical Into A Fundraising Powerhouse. Whether You're Swapping Your Device For A Classic Handset, Hosting A Screen-free Game Night, Or Challenging Friends To A Digital-free Day, Your Efforts Can Support Mental Health Initiatives Across The Uk</p>
  <div class="ideas">Ideas to get you started:</div>

  <div class="idea-card" style="left:147px;top:277px;width:433px;height:120px">
    <svg width="40" height="50" viewBox="0 0 40 50" fill="none" stroke="#7aa0b8" stroke-width="1.6"><rect x="9" y="3" width="22" height="42" rx="4"/><line x1="16" y1="8" x2="24" y2="8"/><circle cx="20" cy="26" r="7"/><path d="M20 22v4l3 2"/></svg>
    <div><h3>Digital Detox Challenge</h3><p>Get sponsored to go smartphone-free for a day, a week, or the entire month.</p></div>
  </div>
  <div class="idea-card" style="left:620px;top:277px;width:434px;height:120px">
    <svg width="44" height="50" viewBox="0 0 44 50" fill="none" stroke="#7aa0b8" stroke-width="1.6"><circle cx="12" cy="14" r="6"/><circle cx="30" cy="10" r="7"/><path d="M27 7l6 3-6 3z"/><path d="M4 44c0-10 5-16 12-16s10 4 12 10"/><path d="M24 30c3-3 8-4 14-2"/></svg>
    <div><h3>Screen-Free Socials</h3><p>Host events like board game nights, book clubs, or outdoor adventures.</p></div>
  </div>
  <div class="idea-card" style="left:144px;top:426px;width:912px;height:120px">
    <svg width="44" height="50" viewBox="0 0 44 50" fill="none" stroke="#7aa0b8" stroke-width="1.6"><path d="M22 4l16 6v12c0 12-8 20-16 24C14 42 6 34 6 22V10z"/><line x1="12" y1="22" x2="32" y2="22"/><line x1="22" y1="14" x2="22" y2="36"/></svg>
    <div><h3>Workplace Warriors</h3><p>Encourage colleagues to join the movement and match funds raised. Need inspiration? Our fundraising toolkit is packed with tips, templates, &amp; resources to help you succeed.</p></div>
  </div>
</section>

<section class="donate split abs">
  <h2 class="panel-title heading" style="left:144px;top:58px">Donate</h2>
  <p class="panel-text" style="left:144px;top:116px;width:420px">Every Contribution Fuels Our Mission To Promote Healthier Digital Habits &amp; Support Mental Well-being.</p>
  <div class="label" style="left:144px;top:193px">Ways to give:</div>
  <div class="item" style="left:144px;top:234px;width:420px"><h4>One-Time Donation</h4><p>Support the cause with a single gift.</p></div>
  <div class="item" style="left:144px;top:299px;width:400px"><h4>Monthly Giving</h4><p>Become A Regular Supporter and Help Sustain Our Year round Initiatives.</p></div>
  <div class="item" style="left:144px;top:393px;width:440px"><h4>In Honour</h4><p>Donate in honour of someone embracing the analogue lifestyle.</p></div>
  <div class="photo" style="left:600px;top:0;width:600px;height:524px;background:linear-gradient(135deg,#2a2a2a,#4a4a4a 40%,#7a2020 55%,#3a3a3a 80%,#222)" role="img" aria-label="Photo of a red rotary telephone and a vintage mobile phone in front of a red and grey wall"></div>
</section>

<section class="resources split abs">
  <div class="photo" style="left:0;top:0;width:598px;height:538px;background:linear-gradient(135deg,#2c4a66,#3f6285 45%,#a0342c 75%,#6c2620)" role="img" aria-label="Photo of a smiling man in a flat cap and red jumper holding a portable cassette player"></div>
  <h2 class="panel-title heading" style="left:666px;top:45px">Resource Tips</h2>
  <p class="panel-text" style="left:666px;top:101px;width:400px">Embarking on a digital detox? We've got your back. Our resource hub offers practical tips and tools to help you navigate the analogue life.</p>
  <div class="label" style="left:666px;top:207px">Top resources:</div>
  <div class="item" style="left:666px;top:245px;width:390px"><h4>Analogue Starter Kit</h4><p>Guides to help you transition smoothly.</p></div>
  <div class="item" style="left:666px;top:311px;width:390px"><h4>Daily Challenges</h4><p>Fun tasks to keep you engaged and motivated.</p></div>
  <div class="item" style="left:666px;top:381px;width:390px"><h4>Community Stories</h4><p>Read about others' journeys and share your own.</p></div>
  <div class="link">Explore Our Full Range of Resources To Make The Most of Your Pebblestone June Experience</div>
</section>

<section class="events split abs">
  <h2 class="section-title heading">Events</h2>
  <p class="intro">Join The Movement In Person! Our Events Are Designed To Bring People Together, Away From Screens, To Connect &amp; Celebrate.</p>
  <div class="upcoming">Upcoming highlights:</div>

  <div class="slider-btn" style="left:101px"><svg width="8" height="12" viewBox="0 0 8 12"><path d="M6 1L1 6l5 5" stroke="#fff" stroke-width="1.5" fill="none"/></svg></div>
  <div class="slider-btn" style="left:1076px"><svg width="8" height="12" viewBox="0 0 8 12"><path d="M2 1l5 5-5 5" stroke="#fff" stroke-width="1.5" fill="none"/></svg></div>

  <div class="event-card" style="left:144px;width:435px;background:linear-gradient(135deg,#6f5a48,#9a8268 45%,#2f4a3c 75%,#5c4536)" role="img" aria-label="Photo of older friends laughing around a table with food at a launch party"></div>
  <div class="event-tag" style="left:199px;top:2833px;margin-top:-2359px;width:326px;height:37px;line-height:37px;font-size:15px">Launch Party</div>

  <div class="event-card" style="left:621px;width:433px;background:linear-gradient(135deg,#5a4a3e,#8c7260 40%,#b59a84 70%,#6e5848)" role="img" aria-label="Photo of a cheerful group of people of different ages gathered together outdoors"></div>
  <div class="event-tag" style="left:650px;top:401px;width:375px;height:113px;border-bottom:4px solid var(--cyan);padding-top:22px">
    <div style="font-size:15px;font-weight:500">Community Meetups</div>
    <p style="font-size:13px;line-height:23px;color:#555;margin:10px auto 0;width:310px">Engage with others in your area embracing the analogue lifestyle.</p>
  </div>
</section>

<section class="funds split abs">
  <h2 class="title heading">Where Do Funds Go</h2>
  <div class="sub">UK charities and initiatives:</div>
  <div class="nav">
    <svg width="34" height="34" viewBox="0 0 34 34"><path d="M31 3L3 17l28 14z" fill="none" stroke="#bbb" stroke-width="1.5"/></svg>
    <svg width="34" height="34" viewBox="0 0 34 34"><path d="M3 3l28 14L3 31z" fill="var(--cyan)"/></svg>
  </div>
  <div class="charity" style="left:144px">
    <div class="thumb" style="background:linear-gradient(135deg,#2a2a2a,#6a6a6a 50%,#3a3a3a)" role="img" aria-label="Photo of a vintage film camera with lenses"></div>
    <h4>Bright Feeds</h4>
    <p>Delivers interactive sessions in schools to help students, parents, &amp;teachersnavigate social media positively, addressing issues like addiction &amp; online behaviour</p>
  </div>
  <div class="charity" style="left:454px">
    <div class="thumb" style="background:linear-gradient(135deg,#b08a66,#d8c2a6 50%,#8a6a4c)" role="img" aria-label="Photo of a cassette tape on a wooden surface"></div>
    <h4>Netwise Kids</h4>
    <p>Empowers children and young people to navigate the internet safely, providing educational resources and working with stakeholders to prioritise young people's online rights</p>
  </div>
  <div class="charity" style="left:764px">
    <div class="thumb" style="background:linear-gradient(135deg,#e8e8e8,#bfbfbf 50%,#5a5a5a)" role="img" aria-label="Photo of a black rotary telephone surrounded by old mobile phones"></div>
    <h4>Online Compass</h4>
    <p>Offers advice and resources to parents and professionals to keep children safe online, collaborating with major internet service providers and participating in initiatives like the National Online Safety Forum</p>
  </div>
</section>

<section class="strategic split abs">
  <h2 class="panel-title heading">Strategic Allocation<br>of Funds</h2>
  <div class="item" style="left:144px;top:165px;width:430px"><h4>Educational Workshops</h4><p>Fund sessions in schools to educate students, parents, and teachers on digital well-being.</p></div>
  <div class="item" style="left:144px;top:257px;width:430px"><h4>Resource Development</h4><p>Support the creation of toolkits and materials that promote healthy digital habits.</p></div>
  <div class="item" style="left:144px;top:351px;width:430px"><h4>Mental Health Support</h4><p>Invest in programs that offer mental health resources tailored to the challenges posed by digital life</p></div>
  <div class="photo" style="left:600px;top:0;width:600px;height:475px;background:linear-gradient(135deg,#4d3a2c,#7a5a40 40%,#2f5560 70%,#4a3a30)" role="img" aria-label="Photo of a laughing couple relaxing on a sofa reading books together"></div>
</section>

<footer class="site-footer abs">
  <div class="brand"><span class="brand-square"></span>Pebblestone June</div>
  <div class="contact" style="left:648px">
    <svg width="28" height="28" viewBox="0 0 28 28"><circle cx="14" cy="14" r="13" fill="none" stroke="#8fb3c8" stroke-width="1.4"/><path d="M10 8c-1 1-1 3 1 6s4 5 6 6c1 0 2-1 2-2l-2-2-2 1c-1-1-2-2-3-4l1-2-2-2z" fill="#8fb3c8"/></svg>
    +44-000-000-0000
  </div>
  <div class="contact" style="left:837px">
    <svg width="28" height="28" viewBox="0 0 28 28"><circle cx="14" cy="14" r="13" fill="none" stroke="#8fb3c8" stroke-width="1.4"/><rect x="8" y="10" width="12" height="9" fill="#8fb3c8"/><path d="M8 10l6 5 6-5" stroke="#fff" stroke-width="1" fill="none"/></svg>
    contact@pebblestonejune.example
  </div>
  <div class="rule"></div>
  <div class="copy">2025 Copyright - &nbsp;Pebblestone June &nbsp;| All Rights Reserved</div>
</footer>

</body>
</html>
```